Travel Group 'Lydgate Group' needs a new business card design

Lydgate Group is a diverse business specialising in bespoke, tailor made holidays to suit all budgets and we are specialists in planning exciting day/short trips to suit all markets. Our target market is very varied going from the corporate client and as well as people in the community who simply want to experience something special.
We are looking for a card design that will encourage people to look at our websites and social media platforms and to see for themselves the different facets to our business. It is essential that the card has social media icons for Facebook, Twitter and Instagram. We are looking for a card with a blank background with no pictures and for the front side to have the attached Lydgate logo. The card should have similar colour scheme to the attached Lydgate logo.
The card must have the following information on one side:
Maud Penrose
Business Development Manager
maudpenrose@lydgatevoyages.example
Lydgate Group, 87 Quarry Lane
Brackenholm, Glenmoray, Scotland KA19 4TN
+44 (0)1632 730182
And then the card must have the following on the second side:
(Lydgate logo)
(social media icons)
www.lydgatevoyages.example
www.lydgateoutings.example
Target Market(s)
Our target market is very varied going from the corporate client and as well as people in the community who simply want to experience something special.
Industry/Entity Type
Business
Contact Information for Business Card
Maud Penrose
+44 (0)1632 730182
(Lydgate logo)
(social media icons)
www.lydgatevoyages.example
www.lydgateoutings.example
Requirements
Must have
- It is essential that the card has social media icons for Facebook, Twitter & Instagram.
Should not have
- Should not have any images other than Lydgate logo.

```html
<!DOCTYPE html>
<html lang="en">
<head>
<meta charset="utf-8">
<title>Lydgate Group – Business Card</title>
<link rel="stylesheet" href="https://fonts.googleapis.com/css2?family=Alegreya:wght@400;700;800&display=swap">
<style>
  :root {
    --pink: #e2449a;
    --navy: #2a2360;
    --violet: #6a4aa0;
    --white: #ffffff;
    --line: rgba(255,255,255,0.85);
  }
  * { margin: 0; padding: 0; box-sizing: border-box; }
  html, body { width: 1050px; height: 1200px; overflow: hidden; background: var(--white); }
  body { font-family: "Alegreya", Georgia, serif; color: var(--white); }

  .card { position: relative; width: 1050px; height: 1200px; }

  .logo-panel {
    position: absolute; left: 0; top: 0; width: 605px; height: 600px;
    background: var(--white);
  }
  .brand-name {
    position: absolute; left: 188px; top: 318px;
    font-weight: 700; font-size: 60px; letter-spacing: 6px;
    color: var(--navy); line-height: 1;
  }

  .web-panel {
    position: absolute; left: 605px; top: 0; width: 445px; height: 600px;
    background: var(--pink);
  }
  .web-links { position: absolute; left: 17px; top: 224px; font-weight: 700; font-size: 26px; line-height: 35px; white-space: nowrap; letter-spacing: 0.6px; }
  .social-row { position: absolute; left: 16px; top: 321px; display: flex; gap: 4px; }
  .social-icon { width: 50px; height: 50px; border: 1.5px solid var(--line); border-radius: 8px; }

  .details-panel {
    position: absolute; left: 0; top: 600px; width: 1050px; height: 600px;
    background: var(--pink); text-align: center;
  }
  .side-tab { position: absolute; top: 93px; width: 28px; height: 262px; background: var(--violet); }
  .side-tab.left { left: 0; border-radius: 0 10px 10px 0; }
  .side-tab.right { right: 0; border-radius: 10px 0 0 10px; }

  .person-name { position: absolute; left: 0; right: 0; top: 140px; font-weight: 700; font-size: 92px; letter-spacing: 4px; line-height: 1; white-space: nowrap; }
  .job-title { position: absolute; left: 0; right: 0; top: 238px; font-weight: 700; font-size: 30px; letter-spacing: 8px; line-height: 1; white-space: nowrap; }
  .email { position: absolute; left: 0; right: 0; top: 276px; font-size: 28px; line-height: 1; }
  .address { position: absolute; left: 0; right: 0; top: 448px; font-size: 28px; line-height: 35px; font-style: normal; }
  .phone { font-weight: 700; font-size: 30px; letter-spacing: 2.5px; }
</style>
</head>
<body>
<main class="card">
  <section class="logo-panel">
    <div class="brand-name">LYDGATE</div>
  </section>

  <section class="web-panel">
    <div class="web-links">
      <div>www.lydgatevoyages.example</div>
      <div>www.lydgateoutings.example</div>
    </div>
    <div class="social-row" aria-label="Social media links">
      <span class="social-icon"></span>
      <span class="social-icon"></span>
      <span class="social-icon"></span>
    </div>
  </section>

  <section class="details-panel">
    <span class="side-tab left"></span>
    <span class="side-tab right"></span>
    <h1 class="person-name">MAUD PENROSE</h1>
    <p class="job-title">BUSINESS DEVELOPMENT MANAGER</p>
    <p class="email">maudpenrose@lydgatevoyages.example</p>
    <address class="address">
      Lydgate Group, 87 Quarry Lane, Brackenholm, Glenmoray,<br>
      Scotland KA19 4TN<br>
      <span class="phone">+44 (0)1632 730182</span>
    </address>
  </section>
</main>
</body>
</html>
```